Penny Harvest

Logo and general packaging design for premium quality, price conscious super foods.

Initial product portfolio includes:

Organic Raw Chia Seeds - Resealable plastic bags with 3 x 5 label.
Organic Cold Pressed Coconut Oil (plastic jar) - 2.5 x 6.5 label

The design should be transferable to additional products.

Project requirements:

The design should be simple and the core trade dress should be no more than 2 or 3 colors. The logo should reproduce well in black/1 color.

The idea of this design is to convey quality and simplicity, like a "no frills", premium quality brand.

Deliverable: fully editable (text and illustration):

Logo.

Basic Jar label design.

Basic Bag label design.

Target Market(s)

Educated women aged 22-45

Industry/Entity Type

Plastic

Requirements
Must have
• Clear, simple logo, delivered in vector form, 1 color/black.
• Use of logo on 1 jar label and 1 bag label, each with product name and space for required and optional marketing content.
Nice to have
• Additional iterations of the design to demonstrate your concept of how we will visually vary additional items in jars and bags.
• i.e. What an additional product in a bag would look like for purposes of brand consistency and product differentiation on shelf or online in e-store.
Should not have
• overly detailed graphics that don't scale well and/or may be hard to read or understand. 4 color design elements (except to simiulate how the product may look through the clear jar or bag or how the product may be placed in a simulated surrounding or ad.

```html
<!DOCTYPE html>
<html lang="en">
<head>
<meta charset="utf-8">
<title>Penny Harvest – Logo and Labels</title>
<link href="https://fonts.googleapis.com/css2?family=Lato:wght@300;400;700;900&display=swap" rel="stylesheet">
<style>
  :root {
    --leaf-green: #95c11f;
    --sky-blue: #3dbdee;
    --seed-yellow: #f2e600;
    --ink: #1a1a1a;
    --paper: #ffffff;
  }
  * { box-sizing: border-box; margin: 0; padding: 0; }
  html, body { width: 1200px; height: 1000px; overflow: hidden; background: var(--paper); }
  body { position: relative; font-family: "Lato", Arial, sans-serif; }

  .top-rule { position: absolute; left: 0; top: 0; width: 1200px; height: 8px; background: var(--leaf-green); }

  .wordmark {
    position: absolute;
    font-weight: 300;
    letter-spacing: 0.09em;
    white-space: nowrap;
    text-transform: uppercase;
    transform: translateX(-50%);
    line-height: 1;
  }
  .wordmark--green { left: 320px; top: 52px; font-size: 38px; color: var(--leaf-green); }
  .wordmark--black { left: 878px; top: 52px; font-size: 38px; color: var(--ink); }

  .label { position: absolute; overflow: hidden; }
  .label--chia { left: 275px; top: 149px; width: 651px; height: 391px; background: var(--leaf-green); }
  .label--coconut { left: 177px; top: 620px; width: 846px; height: 292px; background: var(--sky-blue); }

  .label__tab { position: absolute; top: 0; }
  .label__tab svg { display: block; }

  .label__brand { font-size: 31px; top: 19px; }
  .label--chia .label__brand { left: 313px; color: var(--leaf-green); }
  .label--coconut .label__brand { left: 429px; top: 22px; color: var(--sky-blue); }

  .label__pattern { position: absolute; }
  .label--chia .label__pattern {
    left: 115px; top: 85px; width: 320px; height: 290px;
    background: radial-gradient(ellipse at center, rgba(242,230,0,0.55) 0%, rgba(242,230,0,0.25) 55%, rgba(242,230,0,0) 72%);
  }
  .label--coconut .label__pattern {
    left: 40px; top: 20px; width: 780px; height: 260px;
    background: radial-gradient(ellipse at center, rgba(255,255,255,0.28) 0%, rgba(255,255,255,0.12) 55%, rgba(255,255,255,0) 75%);
  }

  .label__title {
    position: absolute; left: 0; width: 100%;
    text-align: center; color: var(--paper);
    font-weight: 300; white-space: nowrap; line-height: 1;
  }
  .label__title strong { font-weight: 700; }
  .label--chia .label__title { top: 190px; font-size: 38px; padding-left: 26px; }
  .label--coconut .label__title { top: 152px; font-size: 35px; }

  .label__ingredients { position: absolute; color: var(--paper); font-weight: 700; }
  .label--chia .label__ingredients { left: 113px; top: 343px; width: 335px; font-size: 8.3px; line-height: 1.3; }
  .label--coconut .label__ingredients { left: 266px; top: 257px; width: 255px; font-size: 6.3px; line-height: 1.3; }

  .label__weight {
    position: absolute; background: var(--paper);
    font-weight: 900; display: flex; align-items: center; justify-content: center;
  }
  .label--chia .label__weight { left: 458px; top: 339px; width: 72px; height: 52px; font-size: 21px; color: var(--leaf-green); }
  .label--coconut .label__weight { left: 526px; top: 255px; width: 53px; height: 37px; font-size: 16px; color: var(--sky-blue); }
</style>
</head>
<body>
  <div class="top-rule"></div>

  <div class="wordmark wordmark--green">Penny Harvest</div>
  <div class="wordmark wordmark--black">Penny Harvest</div>

  <section class="label label--chia" aria-label="Bag label: Organic Raw Chia Seeds">
    <div class="label__pattern" role="img" aria-label="Scattered yellow chia seed illustration"></div>
    <div class="label__tab" style="left:113px">
      <svg width="422" height="72" viewBox="0 0 422 72"><path d="M0 0 H422 V62 Q211 76 0 62 Z" fill="#ffffff"/></svg>
    </div>
    <div class="wordmark label__brand">Penny Harvest</div>
    <h2 class="label__title"><strong>Organic</strong> Raw Chia Seeds</h2>
    <p class="label__ingredients">Ingredients: 100% organic raw chia seeds. Store in a cool, dry place and reseal the bag after each use. Add to smoothies, yoghurt, oats or baking. Packed in a facility that also handles nuts.</p>
    <div class="label__weight">100g</div>
  </section>

  <section class="label label--coconut" aria-label="Jar label: Organic Cold Pressed Coconut Oil">
    <div class="label__pattern" role="img" aria-label="Scattered white bubble rings pattern"></div>
    <div class="label__tab" style="left:216px">
      <svg width="415" height="74" viewBox="0 0 415 74"><path d="M0 0 H415 V64 Q207 78 0 64 Z" fill="#ffffff"/></svg>
    </div>
    <div class="wordmark label__brand">Penny Harvest</div>
    <h2 class="label__title"><strong>Organic</strong> Cold Pressed Coconut Oil</h2>
    <p class="label__ingredients">Ingredients: 100% organic cold pressed virgin coconut oil. Store below 24°C; melts when warm. Use for cooking, baking or skin care. Keep the lid closed after use and away from sunlight.</p>
    <div class="label__weight">100g</div>
  </section>
</body>
</html>
```